I need a graphic for the promotion email for our "5th Yearly Crisis Preparedness Skills Camp" that incorporates our current logo and brand theme. I would like this graphic to funnel potentional attendees to register for a course. My perference would include a cool fire photo from our facility for the background. More information can be found on Marlowfieldcrew.com and also our Facebook.

```html
<!DOCTYPE html>
<html lang="en">
<head>
<meta charset="utf-8">
<title>5th Yearly Crisis Preparedness Skills Camp</title>
<link href="https://fonts.googleapis.com/css2?family=Oswald:wght@600;700&family=Open+Sans:wght@400;600&family=Montserrat:wght@500;700&display=swap" rel="stylesheet">
<style>
  :root {
    --ink-dark: #0b0807;
    --smoke: #2b2420;
    --ember: #9a3a0c;
    --amber: #c8681a;
    --flame: #f39a22;
    --flame-core: #ffd36a;
    --accent: #e8401c;
    --white: #ffffff;
  }
  * { margin: 0; padding: 0; box-sizing: border-box; }
  html, body { width: 1200px; height: 670px; overflow: hidden; background: var(--ink-dark); }
  .banner {
    position: relative;
    width: 1200px;
    height: 670px;
    overflow: hidden;
    color: var(--white);
    text-align: center;
  }
  .banner-photo {
    position: absolute;
    inset: 0;
    background:
      radial-gradient(ellipse 150px 170px at 780px 330px, rgba(255,211,106,0.95), rgba(243,154,34,0.8) 45%, transparent 100%),
      radial-gradient(ellipse 130px 150px at 700px 380px, rgba(255,211,106,0.85), rgba(243,154,34,0.6) 50%, transparent 100%),
      radial-gradient(ellipse 300px 260px at 820px 300px, rgba(243,154,34,0.9), rgba(200,104,26,0.7) 45%, transparent 85%),
      radial-gradient(ellipse 240px 220px at 1000px 250px, rgba(200,104,26,0.75), rgba(154,58,12,0.45) 55%, transparent 90%),
      radial-gradient(ellipse 230px 260px at 260px 300px, rgba(200,104,26,0.7), rgba(154,58,12,0.45) 50%, transparent 85%),
      radial-gradient(ellipse 160px 200px at 120px 420px, rgba(154,58,12,0.6), transparent 85%),
      radial-gradient(ellipse 650px 150px at 620px 600px, rgba(200,104,26,0.55), rgba(154,58,12,0.3) 55%, transparent 90%),
      radial-gradient(ellipse 260px 160px at 1120px 120px, rgba(154,58,12,0.5), transparent 85%),
      linear-gradient(180deg, #3a2a22 0%, var(--smoke) 30%, #20170f 65%, var(--ink-dark) 100%);
  }
  .banner-shade {
    position: absolute;
    inset: 0;
    background:
      radial-gradient(ellipse 330px 170px at 600px 140px, rgba(0,0,0,0.5), transparent 85%),
      radial-gradient(ellipse 1000px 520px at 600px 335px, transparent 60%, rgba(0,0,0,0.55) 100%);
  }
  .banner-content { position: relative; }
  .edition {
    position: absolute; top: 41px; left: 0; width: 1200px;
    font: 700 37px/1 'Oswald', sans-serif;
    letter-spacing: 0.5px;
    text-shadow: 0 2px 6px rgba(0,0,0,0.7);
  }
  .edition sup { font-size: 19px; vertical-align: 14px; }
  .title {
    position: absolute; left: 0; width: 1200px;
    font: 700 56px/1 'Oswald', sans-serif;
    letter-spacing: 1px;
    text-shadow: 0 3px 10px rgba(0,0,0,0.75);
  }
  .title-accent { top: 84px; color: var(--accent); }
  .title-main { top: 142px; color: var(--white); }
  .tagline {
    position: absolute; top: 200px; left: 0; width: 1200px;
    font: 400 22px/27px 'Open Sans', sans-serif;
    text-shadow: 0 2px 6px rgba(0,0,0,0.8);
  }
  .host-label {
    position: absolute; top: 305px; left: 0; width: 1200px;
    font: 500 17px/1 'Montserrat', sans-serif;
    text-shadow: 0 2px 5px rgba(0,0,0,0.7);
  }
  .host-mark {
    position: absolute; top: 333px; left: 552px;
    width: 96px; height: 96px;
    border: 6px solid var(--accent);
    border-radius: 50%;
  }
  .host-name {
    position: absolute; top: 438px; left: 0; width: 1200px;
    font: 700 31px/1 'Montserrat', sans-serif;
    letter-spacing: 4px;
    color: var(--white);
    text-shadow: 0 2px 6px rgba(0,0,0,0.7);
  }
  .register-btn {
    position: absolute; top: 532px; left: 497px;
    width: 206px; height: 50px;
    background: var(--accent);
    border-radius: 3px;
    font: 600 23px/50px 'Open Sans', sans-serif;
    color: var(--white);
    text-decoration: none;
  }
  .alt-or {
    position: absolute; top: 594px; left: 0; width: 1200px;
    font: 400 15px/1 'Open Sans', sans-serif;
    text-shadow: 0 2px 5px rgba(0,0,0,0.8);
  }
  .details-link {
    position: absolute; top: 615px; left: 0; width: 1200px;
    font: 600 15px/1 'Open Sans', sans-serif;
    color: var(--white);
    text-decoration: none;
    text-shadow: 0 2px 5px rgba(0,0,0,0.8);
  }
</style>
</head>
<body>
<main class="banner">
  <div class="banner-photo" role="img" aria-label="Night photo of firefighters with hose and axe battling a large blaze at an industrial plant"></div>
  <div class="banner-shade"></div>
  <div class="banner-content">
    <p class="edition">5<sup>TH</sup> YEARLY</p>
    <h1>
      <span class="title title-accent">CRISIS PREPAREDNESS</span>
      <span class="title title-main">SKILLS CAMP</span>
    </h1>
    <p class="tagline">REAL-WORLD FIRE &amp; INDUSTRIAL<br>EMERGENCY TRAINING</p>
    <p class="host-label">Hosted by:</p>
    <span class="host-mark"></span>
    <p class="host-name">MARLOWFIELD CREW</p>
    <a class="register-btn" href="#">REGISTER NOW</a>
    <p class="alt-or">Or</p>
    <a class="details-link" href="#">CHECK COURSE DETAILS</a>
  </div>
</main>
</body>
</html>
```